Affiliate marketing network landing page

We need a landing page for an affiliate marketing company called Vantor Crestline.

Our primary offering will be a CPA (cost per action) affiliate network with emphasis on treating our affiliates EPC's "royally".

We would like the final design to be clean and minimal similar to the aesthetic of plumwick.com or breezomarkup.com.

Some of our competitors/other companies in the industry for inspiration would be tarvemunda.com, yieldotterpack.com, pertubix.com, tapvaulty.com, glorvinhaus.com, nudgemerchy.com, promvetted.com to name a few in no particular order.

Should you propose the winning design, we would like you to build it just in HTML/CSS (not to be integrated into a CMS) - but we can discuss the specifics of that when the time comes.

Attached is the logo that should be used both on the site and as inspiration for the design (colors, aesthetic, etc).

```html
<!DOCTYPE html>
<html lang="en">
<head>
<meta charset="utf-8">
<title>Vantor Crestline — Payments infrastructure for the internet</title>
<link href="https://fonts.googleapis.com/css2?family=Poppins:wght@400;500;600;700&display=swap" rel="stylesheet">
<style>
:root{
  --ink:#1d1d21;
  --ink-soft:#3a3a3e;
  --text:#222226;
  --muted:#7a7a80;
  --line:#e6e6ea;
  --grey:#9a9b9f;
  --grey-btn:#8d8e93;
  --grey-light:#c9cace;
  --red:#e0404f;
  --red-deep:#8a0f22;
  --white:#ffffff;
  --card-shadow:0 14px 34px rgba(20,20,30,.14);
}
*{box-sizing:border-box;margin:0;padding:0}
html,body{width:1200px;height:4474px;overflow:hidden;background:var(--white)}
body{font-family:'Poppins',sans-serif;color:var(--text)}
.page{position:relative;width:1200px;height:4474px;overflow:hidden}
.abs{position:absolute}
.bg-shape{position:absolute;left:0;top:0}
.brand{color:var(--white);font-weight:500;letter-spacing:4px;font-size:15px;text-transform:uppercase}
.nav a{position:absolute;top:47px;color:var(--white);font-size:12.5px;font-weight:500;text-decoration:none;letter-spacing:.2px}
.btn{position:absolute;display:flex;align-items:center;justify-content:center;border-radius:22px;font-size:11px;font-weight:600;letter-spacing:.4px;text-transform:uppercase;color:var(--white);background:var(--grey-btn)}
.btn-dark{background:#4a4a4f}
.btn-ghost{background:none}
.hero-title{left:87px;top:205px;color:var(--white);font-size:57px;line-height:66px;font-weight:700;letter-spacing:-.3px}
.hero-sub{left:87px;top:416px;color:#e8e8ec;font-size:12px;line-height:22px;width:420px}
.card{position:absolute;background:var(--white);border-radius:14px;box-shadow:var(--card-shadow)}
.eyebrow{position:absolute;font-size:12.5px;font-weight:600;color:var(--muted)}
.h2{position:absolute;font-size:29px;line-height:40px;font-weight:600;color:var(--text)}
.body{position:absolute;font-size:12.5px;line-height:21px;color:#76767c}
.feature h3{font-size:14px;font-weight:600;margin:14px 0 10px;color:var(--text)}
.feature p{font-size:12.5px;line-height:21px;color:#76767c}
.feature{position:absolute;width:200px}
.divider{position:absolute;left:87px;width:1024px;height:1px;background:var(--line)}
.link{font-size:12px;font-weight:600;color:#9a9aa0;text-decoration:underline}
.stat{position:absolute;color:var(--white)}
.stat b{display:block;font-size:29px;font-weight:600;line-height:34px}
.stat span{font-size:13px;color:#f0f0f2}
.mini-label{font-size:8px;color:#9a9aa0}
.partner{position:absolute;display:flex;align-items:center;gap:6px;font-size:22px;font-weight:600}
.partner i{display:inline-block;width:12px;height:12px;border-radius:50%}
.footer-col{position:absolute;top:4078px;color:var(--white)}
.footer-col h4{font-size:17px;font-weight:600;margin-bottom:22px}
.footer-col li{list-style:none;font-size:12px;line-height:31px}
.social{position:absolute;top:4250px;width:38px;height:38px;border-radius:50%;background:#2d2d31}
.dash-stat{position:absolute;top:26px}
.dash-stat small{display:block;font-size:7.5px;color:#9a9aa0;margin-bottom:10px}
.dash-stat b{font-size:14px;font-weight:600}
.dash-stat em{font-style:normal;font-size:7.5px;color:#8a8a90;margin-left:30px}
.tile{position:absolute;top:262px;width:92px;height:62px;border-radius:8px;background:#a9aaae;color:var(--white);font-size:8.5px;display:flex;flex-direction:column;align-items:center;justify-content:flex-end;padding-bottom:8px;gap:8px}
.tile.active{background:#3a3a3e}
</style>
</head>
<body>
<div class="page">

  <svg class="bg-shape" width="1200" height="720" viewBox="0 0 1200 720" aria-hidden="true">
    <defs>
      <linearGradient id="heroGlow" x1="0" y1="1" x2="1" y2="0">
        <stop offset="0" stop-color="#9b1026" stop-opacity=".9"/>
        <stop offset=".45" stop-color="#5a0b18" stop-opacity=".6"/>
        <stop offset="1" stop-color="#1d1d21" stop-opacity="0"/>
      </linearGradient>
      <linearGradient id="heroGlow2" x1="0" y1="1" x2="1" y2="0">
        <stop offset="0" stop-color="#1d1d21" stop-opacity="0"/>
        <stop offset=".6" stop-color="#a8122b" stop-opacity=".85"/>
        <stop offset="1" stop-color="#3a0a14" stop-opacity=".3"/>
      </linearGradient>
    </defs>
    <polygon points="0,0 1200,0 1200,512 0,705" fill="#1d1d21"/>
    <polygon points="0,705 0,600 700,420 560,600" fill="url(#heroGlow)"/>
    <polygon points="500,630 1200,470 1200,512 500,630" fill="url(#heroGlow2)"/>
    <polygon points="820,520 1200,420 1200,440 900,520" fill="url(#heroGlow2)" opacity=".5"/>
  </svg>

  <header>
    <div class="abs brand" style="left:100px;top:68px">Vantor Crestline</div>
    <nav class="nav">
      <a style="left:485px">PRODUCTS</a>
      <a style="left:587px">USE CASES</a>
      <a style="left:690px">DEVELOPERS</a>
      <a style="left:800px">COMPANY</a>
      <a style="left:899px">PRICING</a>
    </nav>
    <div class="btn btn-dark" style="left:1007px;top:35px;width:103px;height:40px;font-size:11px">Sign in&nbsp;›</div>
  </header>

  <section class="hero">
    <h1 class="abs hero-title">Payments<br>infrastructure<br>for the internet</h1>
    <p class="abs hero-sub">Millions of companies of all sizes—from startups to Summit 500s—use Plumwick's software and APIs</p>
    <div class="btn" style="left:87px;top:488px;width:123px;height:38px">Start now</div>
    <div class="btn btn-ghost" style="left:214px;top:488px;width:130px;height:38px">Contact sales</div>

    <div class="card" style="left:660px;top:172px;width:408px;height:401px;border-radius:12px">
      <div class="abs" style="left:0;top:0;width:408px;height:36px;background:#e9e9ec;border-radius:12px 12px 0 0"></div>
      <div class="abs" style="left:24px;top:14px;display:flex;gap:6px"><i style="width:6px;height:6px;border-radius:50%;background:#fff"></i><i style="width:6px;height:6px;border-radius:50%;background:#fff"></i><i style="width:6px;height:6px;border-radius:50%;background:#fff"></i></div>
      <div class="abs" style="left:43px;top:62px;font-size:21px;font-weight:500">Last 7 days</div>
      <div class="abs mini-label" style="left:120px;top:116px">Report Summary</div>
      <div class="abs mini-label" style="left:247px;top:116px">Total Balance to Payout</div>
      <div class="abs" style="left:247px;top:140px;width:60px;height:6px;background:#eee;border-radius:3px"></div>
      <div class="abs" style="left:247px;top:154px;width:36px;height:6px;background:#eee;border-radius:3px"></div>
      <div class="abs mini-label" style="left:100px;top:194px">Sales by Client</div>
      <div class="abs" style="left:100px;top:218px;width:130px;height:6px;background:#f0f0f2;border-radius:3px"></div>
      <div class="abs" style="left:100px;top:240px;width:110px;height:6px;background:#f0f0f2;border-radius:3px"></div>
      <div class="abs" style="left:100px;top:262px;width:120px;height:6px;background:#f0f0f2;border-radius:3px"></div>
      <div class="abs" style="left:100px;top:284px;width:90px;height:6px;background:#f0f0f2;border-radius:3px"></div>
    </div>

    <div class="card" style="left:592px;top:271px;width:153px;height:177px">
      <div class="abs" style="left:18px;top:20px;font-size:12px;font-weight:600">Earnings</div>
      <div class="abs" style="left:18px;top:50px;font-size:19px;font-weight:500">$9677.04</div>
      <div class="abs" style="left:18px;top:80px;font-size:8px;color:#8a8fbf">Views</div>
      <svg class="abs" style="left:18px;top:112px" width="120" height="40" viewBox="0 0 120 40">
        <g fill="#f3b8be"><rect x="0" y="18" width="4" height="22"/><rect x="24" y="10" width="4" height="30"/><rect x="42" y="6" width="4" height="34"/><rect x="60" y="22" width="4" height="18"/><rect x="84" y="14" width="4" height="26"/><rect x="102" y="20" width="4" height="20"/></g>
        <g fill="#d8d8de"><rect x="8" y="24" width="4" height="16"/><rect x="32" y="20" width="4" height="20"/><rect x="50" y="14" width="4" height="26"/><rect x="70" y="8" width="4" height="32"/><rect x="92" y="24" width="4" height="16"/><rect x="110" y="16" width="4" height="24"/></g>
        <g fill="#e0404f"><rect x="16" y="12" width="4" height="28"/><rect x="78" y="4" width="4" height="36"/></g>
      </svg>
    </div>

    <div class="card" style="left:908px;top:380px;width:203px;height:207px">
      <div class="abs" style="left:16px;top:28px;font-size:12px;font-weight:600">Statistics</div>
      <div class="abs" style="left:148px;top:28px;padding:2px 8px;border-radius:8px;background:#fde8ea;color:#e0404f;font-size:8px;font-weight:600">PDF</div>
      <div class="abs" style="left:16px;top:50px;font-size:8.5px;color:#8a8fbf">Payments Report</div>
      <svg class="abs" style="left:28px;top:78px" width="160" height="120" viewBox="0 0 160 120">
        <g fill="#d6d9ec"><rect x="0" y="22" width="10" height="70" rx="5"/><rect x="52" y="50" width="10" height="42" rx="5"/><rect x="78" y="40" width="10" height="52" rx="5"/><rect x="104" y="58" width="10" height="34" rx="5"/><rect x="130" y="70" width="10" height="22" rx="5"/></g>
        <rect x="26" y="4" width="10" height="88" rx="5" fill="#e0404f"/>
        <circle cx="31" cy="100" r="3" fill="#e0404f"/>
        <g fill="#b0b0b8" font-size="8" font-family="Poppins,sans-serif"><text x="0" y="117">67</text><text x="26" y="117">72</text><text x="52" y="117">52</text><text x="78" y="117">47</text><text x="104" y="117">28</text><text x="130" y="117">27</text></g>
      </svg>
    </div>

    <div class="card" style="left:636px;top:528px;width:210px;height:163px">
      <div class="abs" style="left:16px;top:22px;font-size:12px;font-weight:500">Growth</div>
      <svg class="abs" style="left:14px;top:44px" width="184" height="110" viewBox="0 0 184 110">
        <defs><linearGradient id="gFill" x1="0" y1="0" x2="0" y2="1"><stop offset="0" stop-color="#f4a1aa" stop-opacity=".5"/><stop offset="1" stop-color="#fff" stop-opacity="0"/></linearGradient></defs>
        <path d="M0 50 C12 30 22 48 34 46 S52 28 60 36 S76 52 88 42 S104 30 112 32 S128 28 140 20 S168 10 176 0 L176 68 L0 68Z" fill="url(#gFill)"/>
        <path d="M0 50 C12 30 22 48 34 46 S52 28 60 36 S76 52 88 42 S104 30 112 32 S128 28 140 20 S168 10 176 0" fill="none" stroke="#e0404f" stroke-width="1.6"/>
        <circle cx="140" cy="20" r="3" fill="#fff" stroke="#e0404f"/>
        <rect x="40" y="80" width="120" height="3" rx="1.5" fill="#eee"/>
        <circle cx="44" cy="81.5" r="3" fill="#f2a36b"/><circle cx="110" cy="81.5" r="3" fill="#e0404f"/>
        <g fill="#b8b8c0" font-size="8" font-family="Poppins,sans-serif"><text x="2" y="104">67</text><text x="28" y="104">72</text><text x="54" y="104">52</text><text x="80" y="104">47</text><text x="106" y="104">28</text><text x="132" y="104">27</text><text x="158" y="104">37</text></g>
      </svg>
    </div>
  </section>

  <section class="why">
    <div class="eyebrow" style="left:0;width:1200px;text-align:center;top:787px">Why Vantor Crestline</div>
    <h2 class="h2" style="left:0;width:1200px;text-align:center;top:815px">A technology-first approach to<br>payments and finance</h2>

    <div class="feature" style="left:122px;top:935px">
      <svg width="44" height="44" viewBox="0 0 44 44"><circle cx="22" cy="22" r="8" fill="#6a6a70"/><g fill="#9a9aa0"><circle cx="22" cy="6" r="4"/><circle cx="22" cy="38" r="4"/><circle cx="6" cy="22" r="4"/><circle cx="38" cy="22" r="4"/><circle cx="10" cy="10" r="3"/><circle cx="34" cy="34" r="3"/><circle cx="34" cy="10" r="3"/><circle cx="10" cy="34" r="3"/></g></svg>
      <h3>Close to the metal</h3>
      <p>Aenean sollicitudin, lorem quis bibendum auctor nisi elit nibh id elit duis sed odio sit</p>
    </div>
    <div class="feature" style="left:373px;top:935px">
      <svg width="44" height="44" viewBox="0 0 44 44"><polygon points="4,4 26,22 4,40" fill="#b0b0b6"/><polygon points="18,10 42,22 18,34" fill="#5e5e64"/></svg>
      <h3>Close to the metal</h3>
      <p>Aenean sollicitudin, lorem quis bibendum auctor nisi elit nibh id elit duis sed odio sit</p>
    </div>
    <div class="feature" style="left:625px;top:935px">
      <svg width="44" height="44" viewBox="0 0 44 44"><circle cx="20" cy="24" r="17" fill="#c8c8cd"/><path d="M6 26 L14 26 L18 18 L22 32 L26 22 L34 22" fill="none" stroke="#fff" stroke-width="2.4"/><circle cx="35" cy="10" r="8" fill="#4a4a50"/><path d="M32 7 L38 13 M38 7 L32 13" stroke="#fff" stroke-width="1.6"/></svg>
      <h3>Close to the metal</h3>
      <p>Aenean sollicitudin, lorem quis bibendum auctor nisi elit nibh id elit duis sed odio sit</p>
    </div>
    <div class="feature" style="left:873px;top:935px">
      <svg width="44" height="44" viewBox="0 0 44 44"><circle cx="22" cy="22" r="16" fill="#5e5e64" stroke="#9a9aa0" stroke-width="5" stroke-dasharray="4 3"/><circle cx="22" cy="22" r="7" fill="#b0b0b6"/></svg>
      <h3>Close to the metal</h3>
      <p>Aenean sollicitudin, lorem quis bibendum auctor nisi elit nibh id elit duis sed odio sit</p>
    </div>
  </section>

  <div class="divider" style="top:1160px"></div>

  <section class="unified">
    <div class="eyebrow" style="left:175px;top:1242px">Unified platform</div>
    <h2 class="h2" style="left:175px;top:1269px;font-size:28px">A fully integrated suite of<br>payments products</h2>
    <div class="btn" style="left:175px;top:1381px;width:195px;height:38px;font-size:10.5px">Start with payments</div>
    <p class="body" style="left:611px;top:1264px;width:415px;line-height:22.2px">Aenean sollicitudin, lorem quis bibendum auctor, nisi elit consequat ipsum, nec sagittis sem nibh id elit. Duis sed odio sit amet nibh vulputate cursus a sit amet mauris. Morbi accumsan ipsum velit. Nam nec tellus a odio tincidunt auctor a ornare odio. Sed non  mauris vitae erat consequat auctor eu in elit. Class aptent taciti sociosqu...</p>
  </section>

  <svg class="bg-shape" style="top:1945px" width="1200" height="710" viewBox="0 0 1200 710" aria-hidden="true">
    <polygon points="0,0 1200,0 1200,705 0,575" fill="#9a9b9f"/>
  </svg>
  <div class="abs" role="img" aria-label="Wireframe globe of connected network points" style="left:-10px;top:2049px;width:531px;height:556px;border-radius:50%;background:radial-gradient(circle at 55% 40%, rgba(255,255,255,.55), rgba(255,255,255,.18) 55%, rgba(255,255,255,0) 72%)"></div>

  <section class="showcase">
    <div class="abs" style="left:59px;top:1509px;width:292px;height:189px;border-radius:12px;background:#9a9b9f;color:#fff;overflow:hidden">
      <div class="abs" style="left:26px;top:20px;font-size:14px;font-weight:500">Fernlow</div>
      <div class="abs" style="left:34px;top:66px;width:34px;height:28px;border-radius:5px;background:#e4e4e8"></div>
      <div class="abs" style="left:112px;top:66px;width:30px;height:30px;border-radius:50%;background:#fff"></div>
      <div class="abs" style="left:26px;top:150px;font-size:9.5px;font-weight:600">Ines Haverly</div>
      <div class="abs" style="right:20px;top:142px;font-size:20px;font-weight:700">Carduna</div>
    </div>

    <div class="card" style="left:827px;top:1551px;width:137px;height:139px;border-radius:10px">
      <div class="abs" style="left:18px;top:16px;width:18px;height:18px;border-radius:50%;background:#e7ecfb"></div>
      <div class="abs" style="left:18px;top:58px;font-size:15px;font-weight:600">14.8k</div>
      <div class="abs" style="left:18px;top:80px;font-size:7.5px;color:#8a8a90">Total users</div>
      <svg class="abs" style="left:0;top:96px" width="137" height="40" viewBox="0 0 137 40"><path d="M0 30 C14 18 22 26 34 28 S50 10 62 22 S78 36 92 24 S108 4 118 14 S130 26 137 22" fill="none" stroke="#3d6ef0" stroke-width="1.5"/></svg>
    </div>

    <div class="card" style="left:269px;top:1747px;width:139px;height:137px;border-radius:10px">
      <div class="abs" style="left:18px;top:16px;width:18px;height:18px;border-radius:50%;background:#fdf3d2"></div>
      <div class="abs" style="left:18px;top:56px;font-size:15px;font-weight:600">32.6k</div>
      <div class="abs" style="left:18px;top:78px;font-size:7.5px;color:#8a8a90">Average reach per post</div>
      <svg class="abs" style="left:0;top:96px" width="139" height="40" viewBox="0 0 139 40"><path d="M0 32 C12 20 22 18 34 24 S52 36 64 22 S84 8 96 18 S118 36 139 28" fill="none" stroke="#f2c200" stroke-width="1.6"/></svg>
    </div>

    <div class="abs" style="left:380px;top:1643px;width:535px;height:344px;border-radius:22px;background:#f1f1f3;box-shadow:var(--card-shadow);z-index:2">
      <div class="abs" style="left:8px;top:8px;right:8px;bottom:8px;border-radius:16px;background:#fff;border-left:30px solid #3a3a3e">
        <div class="dash-stat" style="left:30px"><small>Total Sales</small><b>$18 378</b><em>+14% ↑</em></div>
        <div class="dash-stat" style="left:176px"><small>Sales Today</small><b>$190</b><em>−6% ↓</em></div>
        <div class="dash-stat" style="left:322px"><small>Total Clicks</small><b>45</b><em>+0.36% ↑</em></div>
        <div class="abs" style="left:22px;top:98px;width:445px;height:150px;border-radius:10px;box-shadow:0 4px 14px rgba(0,0,0,.06)">
          <div class="abs" style="left:14px;top:14px;font-size:10px;font-weight:600">New client statistic</div>
          <div class="abs" style="left:368px;top:14px;font-size:7px">This week ▾</div>
          <svg class="abs" style="left:14px;top:36px" width="420" height="110" viewBox="0 0 420 110">
            <rect x="0" y="18" width="400" height="40" fill="#f3f3f5"/>
            <path d="M0 60 C40 30 70 30 90 50 S130 90 150 40 S190 10 220 40 S250 70 280 50 S320 30 340 50 S380 60 400 40" fill="none" stroke="#6a6a70" stroke-width="2"/>
            <path d="M0 50 C40 66 80 20 130 48 S200 58 240 36 S320 40 400 56" fill="none" stroke="#c4c4c8" stroke-width="1.5"/>
            <circle cx="140" cy="24" r="3" fill="#3a3a3e"/>
            <text x="132" y="10" font-size="6" font-family="Poppins,sans-serif">+65</text>
            <g font-size="7.5" fill="#555" font-family="Poppins,sans-serif"><text x="10" y="100">S</text><text x="68" y="100">M</text><text x="136" y="100">T</text><text x="196" y="100">W</text><text x="262" y="100">T</text><text x="320" y="100">F</text><text x="382" y="100">S</text></g>
          </svg>
        </div>
        <div class="tile active" style="left:24px"><svg width="18" height="18" viewBox="0 0 18 18"><path d="M2 9 L9 2 L16 9 V16 H2Z" fill="none" stroke="#fff" stroke-width="1.4"/></svg>User Panel</div>
        <div class="tile" style="left:131px"><svg width="18" height="18" viewBox="0 0 18 18"><ellipse cx="9" cy="9" rx="8" ry="5" fill="none" stroke="#fff" stroke-width="1.4"/><circle cx="9" cy="9" r="2" fill="#fff"/></svg>Web Visits</div>
        <div class="tile" style="left:238px"><svg width="18" height="18" viewBox="0 0 18 18"><path d="M4 14 A4 4 0 0 1 5 6 A5 5 0 0 1 14 7 A3.5 3.5 0 0 1 14 14Z" fill="none" stroke="#fff" stroke-width="1.4"/></svg>Cloud Storage</div>
        <div class="tile" style="left:345px"><svg width="18" height="18" viewBox="0 0 18 18"><path d="M9 2 V15 M4 10 L9 15 L14 10" fill="none" stroke="#fff" stroke-width="1.4"/></svg>Updates</div>
      </div>
    </div>

    <div class="abs" style="left:941px;top:1763px;width:200px;height:316px;border-radius:14px;background:#fff;border:3px solid #d8d8dc;z-index:2">
      <div class="abs" style="left:0;width:194px;top:16px;text-align:center;font-size:7px;letter-spacing:2px">ARDENLY OPTICS</div>
      <div class="abs" role="img" aria-label="Pair of eyeglasses" style="left:45px;top:36px;width:104px;height:30px;border-radius:10px;background:linear-gradient(#f1f1f3,#d9d9dd)"></div>
      <div class="abs" style="left:0;width:194px;top:80px;text-align:center;font-size:7px;font-weight:600">Tessel</div>
      <div class="abs" style="left:0;width:194px;top:90px;text-align:center;font-size:6px;color:#999">Purely functional</div>
      <div class="abs" style="left:76px;top:108px;display:flex;gap:5px"><i style="width:6px;height:6px;border-radius:50%;background:#333"></i><i style="width:6px;height:6px;border-radius:50%;background:#777"></i><i style="width:6px;height:6px;border-radius:50%;background:#aaa"></i><i style="width:6px;height:6px;border-radius:50%;border:1px solid #aaa"></i></div>
      <div class="abs" style="left:8px;top:130px;width:178px;height:16px;border-radius:3px;background:#666b73;color:#fff;font-size:7px;display:flex;align-items:center;justify-content:center">Pay</div>
      <div class="abs" style="left:8px;top:160px;width:178px;height:1px;background:#eee"></div>
      <div class="abs" style="left:8px;top:166px;font-size:7px;font-weight:600">Product details</div>
      <div class="abs" style="left:176px;top:166px;font-size:7px">⌄</div>
      <div class="abs" style="left:8px;top:182px;width:178px;font-size:5.5px;line-height:8px;color:#888">What do you get when you combine round lenses, slim temple arms, and a keyhole bridge? A good-looking frame named Tessel.</div>
      <div class="abs" style="left:8px;top:212px;width:178px;font-size:5.5px;line-height:10px;color:#888">• Made from hand-polished cellulose acetate<br>• Polymer-coated screws for durability</div>
    </div>
  </section>

  <section class="global">
    <div class="eyebrow" style="left:643px;top:2125px;color:#fff">Global scale</div>
    <h2 class="h2" style="left:643px;top:2153px;color:#fff;font-size:28px;line-height:37px">Vantor Crestline the backbone for<br>internet business</h2>
    <p class="body" style="left:643px;top:2238px;width:420px;color:#f2f2f4">Aenean sollicitudin, lorem quis bibendum auctor, nisi elit consequat ipsum, nec sagittis sem nibh id elit duis sed odio sit amet nibh vulputate cursus a sit ame...</p>
    <div class="stat" style="left:643px;top:2338px"><b>250M+</b><span>Aenean sollicitudin lorem quis</span></div>
    <div class="stat" style="left:896px;top:2338px"><b>90%</b><span>Aenean sollicitudin lorem quis</span></div>
    <div class="stat" style="left:643px;top:2416px"><b>135+</b><span>Aenean sollicitudin lorem quis</span></div>
    <div class="stat" style="left:896px;top:2416px"><b>35+</b><span>Aenean sollicitudin lorem quis</span></div>
  </section>

  <section class="developers">
    <div class="eyebrow" style="left:89px;top:2732px">Designed for developers</div>
    <h2 class="h2" style="left:89px;top:2761px;font-size:28px;line-height:37px">The world’s most powerful<br>and easy-to-use APIs</h2>
    <p class="body" style="left:89px;top:2847px;width:420px">Aenean sollicitudin, lorem quis bibendum auctor, nisi elit consequat ipsum, nec sagittis sem nibh id elit duis sed odio sit amet nibh vulputate cursus a sit ame...</p>

    <div class="feature" style="left:89px;top:2950px;width:220px">
      <svg width="44" height="40" viewBox="0 0 44 40"><rect x="0" y="4" width="32" height="24" rx="3" fill="#5e5e64"/><path d="M6 12 L12 16 L6 20" fill="none" stroke="#fff" stroke-width="2"/><circle cx="34" cy="30" r="8" fill="#9a9aa0"/></svg>
      <h3 style="margin-top:6px">Tools for every stack</h3>
      <p>Aenean sollicitudin, lorem quis bibendum auctor nisi elit nibh id elit duis sed odio sit</p>
      <div class="link" style="margin-top:18px">See libraries</div>
    </div>
    <div class="feature" style="left:346px;top:2950px;width:220px">
      <svg width="44" height="40" viewBox="0 0 44 40"><polygon points="4,8 20,0 36,8 20,16" fill="#b0b0b6"/><polygon points="4,8 20,16 20,36 4,28" fill="#6a6a70"/><polygon points="36,8 20,16 20,36 36,28" fill="#9a9aa0"/><circle cx="34" cy="30" r="7" fill="#4a4a50"/></svg>
      <h3 style="margin-top:6px">Prebuilt integrations</h3>
      <p>Aenean sollicitudin, lorem quis bibendum auctor nisi elit nibh id elit duis sed odio sit</p>
      <div class="link" style="margin-top:18px">Explore partners</div>
    </div>

    <div class="abs" role="img" aria-label="Coding illustration with large code braces" style="left:764px;top:2733px;width:346px;height:407px;border-radius:6px;box-shadow:var(--card-shadow);background:linear-gradient(#ffffff 0 53%, #3c3c40 53% 100%)"></div>

    <div class="card" style="left:590px;top:2845px;width:212px;height:168px">
      <div class="abs" style="left:16px;top:20px;font-size:12px;font-weight:500">Growth</div>
      <svg class="abs" style="left:14px;top:42px" width="184" height="110" viewBox="0 0 184 110">
        <path d="M0 50 C12 30 22 48 34 46 S52 28 60 36 S76 52 88 42 S104 30 112 32 S128 28 140 20 S168 10 176 0 L176 68 L0 68Z" fill="url(#gFill)"/>
        <path d="M0 50 C12 30 22 48 34 46 S52 28 60 36 S76 52 88 42 S104 30 112 32 S128 28 140 20 S168 10 176 0" fill="none" stroke="#e0404f" stroke-width="1.6"/>
        <circle cx="140" cy="20" r="3" fill="#fff" stroke="#e0404f"/>
        <rect x="40" y="80" width="120" height="3" rx="1.5" fill="#eee"/>
        <circle cx="44" cy="81.5" r="3" fill="#f2a36b"/><circle cx="110" cy="81.5" r="3" fill="#e0404f"/>
        <g fill="#b8b8c0" font-size="8" font-family="Poppins,sans-serif"><text x="2" y="104">67</text><text x="28" y="104">72</text><text x="54" y="104">52</text><text x="80" y="104">47</text><text x="106" y="104">28</text><text x="132" y="104">27</text><text x="158" y="104">37</text></g>
      </svg>
    </div>
  </section>

  <div class="divider" style="top:3235px"></div>

  <section class="get-started">
    <div class="card" style="left:90px;top:3329px;width:273px;height:255px;box-shadow:0 10px 30px rgba(20,20,30,.08)">
      <svg class="abs" style="left:36px;top:38px" width="34" height="34" viewBox="0 0 34 34"><polygon points="4,16 16,4 30,4 30,18 18,30" fill="#5e5e64"/><polygon points="4,16 16,28 10,32 0,22" fill="#b0b0b6"/><circle cx="23" cy="11" r="3" fill="#fff"/></svg>
      <div class="abs" style="left:36px;top:96px;font-size:14px;font-weight:600">Always know what you pay</div>
      <p class="body" style="left:36px;top:124px;width:200px">Aenean sollicitudin, lorem quis bibendum auctor nisi elit nibh id elit duis sed odio sit</p>
      <div class="abs link" style="left:36px;top:202px">Pricing details</div>
    </div>
    <div class="card" style="left:380px;top:3329px;width:275px;height:255px;box-shadow:0 10px 30px rgba(20,20,30,.08)">
      <svg class="abs" style="left:38px;top:38px" width="30" height="34" viewBox="0 0 30 34"><rect x="2" y="2" width="24" height="30" rx="3" fill="#b0b0b6"/><rect x="6" y="8" width="16" height="20" rx="2" fill="#4a4a50"/></svg>
      <div class="abs" style="left:36px;top:96px;font-size:14px;font-weight:600">Start your integration</div>
      <p class="body" style="left:36px;top:124px;width:200px">Aenean sollicitudin, lorem quis bibendum auctor nisi elit nibh id elit duis sed odio sit</p>
      <div class="abs link" style="left:36px;top:202px">Pricing details</div>
    </div>

    <div class="eyebrow" style="left:715px;top:3345px">Our Vantor Crestline</div>
    <h2 class="h2" style="left:715px;top:3373px;font-size:28px">Ready to get started?</h2>
    <p class="body" style="left:715px;top:3444px;width:400px">Aenean sollicitudin, lorem quis bibendum auctor, nisi elit consequat ipsum, nec sagittis sem nibh id elit duis sed odio sit amet nibh vulputate cursus a sit ame...</p>
    <div class="btn" style="left:715px;top:3536px;width:150px;height:38px">Start now</div>
  </section>

  <section class="partners">
    <div class="abs" style="left:362px;top:3690px;width:1px;height:140px;background:var(--line)"></div>
    <div class="abs" style="left:602px;top:3690px;width:1px;height:140px;background:var(--line)"></div>
    <div class="abs" style="left:842px;top:3690px;width:1px;height:140px;background:var(--line)"></div>
    <div class="partner" style="left:180px;top:3700px;color:#3f8a3a"><i style="background:#f08a24"></i>cartvale</div>
    <div class="partner" style="left:430px;top:3700px;color:#1f9ad6;font-size:18px"><i style="background:#1f9ad6"></i>cloudmerit</div>
    <div class="partner" style="left:678px;top:3700px;color:#222">amberline</div>
    <div class="partner" style="left:912px;top:3700px;color:#222"><i style="background:#6b4fa0;border-radius:2px"></i>chatlowe</div>
    <div class="partner" style="left:188px;top:3790px;color:#2c2c2c"><i style="background:#7ab55c;border-radius:2px"></i>storevyn</div>
    <div class="partner" style="left:437px;top:3790px;color:#4285f4">Glimora</div>
    <div class="partner" style="left:695px;top:3790px;color:#e6187a">rydex</div>
    <div class="partner" style="left:918px;top:3790px;color:#2d8cff">meetora</div>
  </section>

  <svg class="bg-shape" style="top:3880px" width="1200" height="594" viewBox="0 0 1200 594" aria-hidden="true">
    <defs>
      <linearGradient id="footGlow" x1="0" y1="1" x2="1" y2="0">
        <stop offset="0" stop-color="#1d1d21" stop-opacity="0"/>
        <stop offset=".6" stop-color="#8a0f22" stop-opacity=".85"/>
        <stop offset="1" stop-color="#b0142e" stop-opacity=".9"/>
      </linearGradient>
    </defs>
    <polygon points="0,178 1200,27 1200,594 0,594" fill="#1d1d21"/>
    <polygon points="400,160 1200,27 1200,90 700,150" fill="url(#footGlow)"/>
    <polygon points="600,150 1200,60 1200,120" fill="url(#footGlow)" opacity=".5"/>
  </svg>

  <footer>
    <div class="abs brand" style="left:108px;top:4190px;font-size:15px;width:230px;text-align:center">Vantor Crestline</div>
    <div class="social" style="left:141px"></div>
    <div class="social" style="left:189px"></div>
    <div class="social" style="left:238px"></div>
    <div class="social" style="left:287px"></div>

    <div class="footer-col" style="left:419px">
      <h4>Getting Started</h4>
      <ul><li>Installation</li><li>Editor Setup</li><li>Using with Preprocessors</li><li>Optimizing for Production</li><li>Browser Support</li><li>Upgrade Guide</li></ul>
    </div>
    <div class="footer-col" style="left:656px">
      <h4>Core Concepts</h4>
      <ul><li>Utility-First Fundamentals</li><li>Handling Hover, Focus, and Other States</li><li>Responsive Design</li><li>Dark Mode</li><li>Reusing Styles</li><li>Adding Custom Styles</li><li>Functions &amp; Directives</li></ul>
    </div>
    <div class="footer-col" style="left:955px">
      <h4>Customization</h4>
      <ul><li>Configuration</li><li>Content Configuration</li><li>Theme Configuration</li><li>Customizing Screens</li><li>Customizing Colors</li><li>Customizing Spacing</li><li>Plugins</li><li>Presets</li></ul>
    </div>

    <div class="abs" style="left:87px;top:4410px;width:1024px;height:1px;background:#35353a"></div>
    <div class="abs" style="left:0;width:1200px;top:4436px;text-align:center;color:#fff;font-size:12px;font-weight:500">Copyright © 2022 Vantor Crestline | All Rights Reserved.</div>
    <div class="abs" style="left:1133px;top:4398px;width:40px;height:40px;border-radius:50%;background:#8d8e93;color:#fff;font-size:12px;display:flex;align-items:center;justify-content:center">⌃</div>
  </footer>

</div>
</body>
</html>
```